Executive search firm in fashion, luxury and retail industry needs logo and card design.

We are a start-up recruiting firm that specializes in the retail and fashion industry, based in New York. We are looking for something that will appeal to CEO level clients and candidates, but that has a little design edge...not overly corporate but still CEO-appropriate. We have clean, sophisticated taste and want a contemporary feel. Happy to have a two sided card. Not afraid of a little color but it should be high-design, not gimmicky and tasteful.

Quillmart Market(s)

CEO's, HR Leaders, in retail, fashion (i.e. Halvorsen, Quillmart, Otto Brevik)

Industry/Entity Type

Professional Service

Contact Information for Business Card

Calloway Ridge Search Partners
Address to be determined
New York, NY 10036

Marta Velard
Managing Director
(555)038-4172
mvelard@callowayridgesearch.example

Font styles to use
Serif
Sans Serif

Requirements
Must have
• clean lines, crisp graphics, some color. Prefer a graphic treatment over a "logo" per se. No pictures, etc.
Nice to have
• double sided design.
Should not have
• Gimmicks, smaltz, goop. Think Gallery of Current Works, not the Dunmore Holdings. No earth tones, as in beige and brown, no pastels. Strong colors are fine in moderation. Grays are good. Jewel tones are good. No red.

```html
<!DOCTYPE html>
<html lang="en">
<head>
<meta charset="utf-8">
<title>Calloway Ridge Search Partners – Business Cards</title>
<link rel="stylesheet" href="https://fonts.googleapis.com/css2?family=Questrial&family=Encode+Sans+Condensed:wght@600&display=swap">
<style>
  :root {
    --backdrop: #d3d3d3;
    --paper: #eeeeef;
    --brand-blue: #075a84;
    --brand-gray: #8a8a8c;
    --ink: #3a3a3c;
    --white: #ffffff;
  }
  * { margin: 0; padding: 0; box-sizing: border-box; }
  html, body { width: 1200px; height: 1000px; overflow: hidden; background: var(--backdrop); }
  .sheet { position: relative; width: 1200px; height: 1000px; }

  .card {
    position: absolute; width: 459px; height: 254px;
    background: var(--paper); overflow: hidden;
    font-family: "Questrial", sans-serif; color: var(--ink);
  }
  .card--front-a { left: 120px; top: 189px; }
  .card--front-b { left: 624px; top: 189px; }
  .card--front-c { left: 120px; top: 542px; }
  .card--back    { left: 624px; top: 542px; background: var(--brand-blue); color: var(--white); }

  .wordmark { position: absolute; color: var(--brand-blue); line-height: 1; }
  .wordmark__name { display: block; font-size: 19px; letter-spacing: 1.6px; }
  .wordmark__sub { display: block; font-size: 11.5px; letter-spacing: 1.4px; margin-top: 5px; }
  .wordmark--right { right: 31px; top: 47px; text-align: right; }
  .wordmark--left { left: 26px; top: 50px; text-align: left; }
  .card--back .wordmark { color: var(--white); top: 46px; }

  .holder { position: absolute; line-height: 1; }
  .holder__name {
    font-family: "Encode Sans Condensed", sans-serif; font-weight: 600;
    font-size: 14.5px; color: var(--brand-blue); letter-spacing: 0.3px;
  }
  .holder__title { font-size: 11.5px; margin-top: 5px; }
  .card--front-a .holder { left: 30px; top: 118px; }
  .card--front-b .holder { left: 30px; top: 177px; }
  .card--front-c .holder { right: 34px; top: 180px; text-align: right; }

  .contacts { position: absolute; list-style: none; font-size: 11.5px; line-height: 14.5px; }
  .contacts li { display: flex; align-items: center; gap: 7px; }
  .contacts svg { width: 11px; height: 11px; flex: none; }
  .card--front-a .contacts { left: 30px; top: 177px; }
  .card--front-b .contacts { right: 31px; top: 177px; }
  .card--front-b .contacts li { flex-direction: row-reverse; }
  .card--front-c .contacts { left: 26px; top: 180px; }

  .footer-band { position: absolute; left: 0; bottom: 0; width: 459px; height: 11px; }

  .back-url { position: absolute; right: 44px; top: 211px; font-size: 11.5px; }
</style>
</head>
<body>
<svg width="0" height="0" style="position:absolute" aria-hidden="true">
  <defs>
    <symbol id="icon-phone" viewBox="0 0 12 12">
      <rect width="12" height="12" rx="2" fill="#075a84"/>
      <path d="M3.6 2.6 L5 4.2 L4.3 5.1 Q5 6.9 6.9 7.7 L7.8 7 L9.4 8.4 L8.5 9.5 Q4.4 9 2.5 3.5 Z" fill="#fff"/>
    </symbol>
    <symbol id="icon-mail" viewBox="0 0 12 12">
      <rect width="12" height="12" rx="2" fill="#075a84"/>
      <rect x="2.3" y="3.4" width="7.4" height="5.2" fill="none" stroke="#fff" stroke-width="0.9"/>
      <path d="M2.3 3.4 L6 6.4 L9.7 3.4" fill="none" stroke="#fff" stroke-width="0.9"/>
    </symbol>
    <symbol id="icon-web" viewBox="0 0 12 12">
      <rect width="12" height="12" rx="2" fill="#075a84"/>
      <circle cx="6" cy="6" r="3.6" fill="none" stroke="#fff" stroke-width="0.8"/>
      <ellipse cx="6" cy="6" rx="1.6" ry="3.6" fill="none" stroke="#fff" stroke-width="0.7"/>
      <path d="M2.4 6 H9.6 M3 4.2 H9 M3 7.8 H9" stroke="#fff" stroke-width="0.6"/>
    </symbol>
  </defs>
</svg>

<main class="sheet">
  <!-- Front, layout A -->
  <section class="card card--front-a">
    <div class="wordmark wordmark--right">
      <span class="wordmark__name">CALLOWAY RIDGE</span>
      <span class="wordmark__sub">SEARCH PARTNERS</span>
    </div>
    <div class="holder">
      <p class="holder__name">MARTA VELARD</p>
      <p class="holder__title">Managing Director</p>
    </div>
    <ul class="contacts">
      <li><svg><use href="#icon-phone"/></svg>(555)038-4172</li>
      <li><svg><use href="#icon-mail"/></svg>mvelard@callowayridgesearch.example</li>
      <li><svg><use href="#icon-web"/></svg>www.callowayridgesearch.example</li>
    </ul>
    <svg class="footer-band" viewBox="0 0 459 11" preserveAspectRatio="none" aria-hidden="true">
      <polygon points="0,0 270,0 260,11 0,11" fill="var(--brand-gray)"/>
      <polygon points="278,0 459,0 459,11 268,11" fill="var(--brand-blue)"/>
    </svg>
  </section>

  <!-- Front, layout B -->
  <section class="card card--front-b">
    <div class="wordmark wordmark--right">
      <span class="wordmark__name">CALLOWAY RIDGE</span>
      <span class="wordmark__sub">SEARCH PARTNERS</span>
    </div>
    <div class="holder">
      <p class="holder__name">MARTA VELARD</p>
      <p class="holder__title">Managing Director</p>
    </div>
    <ul class="contacts">
      <li><svg><use href="#icon-phone"/></svg>(555)038-4172</li>
      <li><svg><use href="#icon-mail"/></svg>mvelard@callowayridgesearch.example</li>
      <li><svg><use href="#icon-web"/></svg>www.callowayridgesearch.example</li>
    </ul>
    <svg class="footer-band" viewBox="0 0 459 11" preserveAspectRatio="none" aria-hidden="true">
      <polygon points="0,0 174,0 164,11 0,11" fill="var(--brand-gray)"/>
      <polygon points="182,0 459,0 459,11 172,11" fill="var(--brand-blue)"/>
    </svg>
  </section>

  <!-- Front, layout C -->
  <section class="card card--front-c">
    <div class="wordmark wordmark--left">
      <span class="wordmark__name">CALLOWAY RIDGE</span>
      <span class="wordmark__sub">SEARCH PARTNERS</span>
    </div>
    <ul class="contacts">
      <li><svg><use href="#icon-phone"/></svg>(555)038-4172</li>
      <li><svg><use href="#icon-mail"/></svg>mvelard@callowayridgesearch.example</li>
      <li><svg><use href="#icon-web"/></svg>www.callowayridgesearch.example</li>
    </ul>
    <div class="holder">
      <p class="holder__name">MARTA VELARD</p>
      <p class="holder__title">Managing Director</p>
    </div>
    <svg class="footer-band" viewBox="0 0 459 11" preserveAspectRatio="none" aria-hidden="true">
      <polygon points="0,0 270,0 260,11 0,11" fill="var(--brand-gray)"/>
      <polygon points="278,0 459,0 459,11 268,11" fill="var(--brand-blue)"/>
    </svg>
  </section>

  <!-- Back -->
  <section class="card card--back">
    <div class="wordmark wordmark--right">
      <span class="wordmark__name">CALLOWAY RIDGE</span>
      <span class="wordmark__sub">SEARCH PARTNERS</span>
    </div>
    <p class="back-url">www.callowayridgesearch.example</p>
  </section>
</main>
</body>
</html>
```